ringfolly circus promotional hand out flyer

Ringfolly..see ( old design website!) web www.ringfolly-example.co.uk needs a hand out flyer to promote our circus and entertainment activities.
we work at festivals and events, schools, parties, private and corporate..dozens of different type events. we are creative and individual company. we also get inundated and do lots of " festival" or themed/ alternative / creative weddings.

we wish to push our own circus shows/ acts and artists/ circus skills workshops/ Festival and event childrens play areas( kid zones) / loud owls soapy spin parties / cabaret tents.
we want people to book our chows and activities at their events!
would like to use logo and some action photos of artists that we can provide. there may be useful photos on website/ Facebook etc too. we may be able to get bigger resolution of some of attached photos but not sure!!
CURRENT NAME OF OUR CIRCUS SHOW IS "the ringfolly circus show" novel eh!? this may change in very near future and may help this design!
plus list of some of activities. and contacts etc.

we sort of have a new tag line.." wild wonders grow under striped roofs!"

Feature words on front..or possibly rear..( happy to have double sided)
Circus. ( in Big Bold circus lettering!) Ringfolly Family Circus Show. Circus Skills Workshops.
Acts, Artists & Attractions. Arena Shows, Festivals. Indoor & Outdoor Events, Schools, Parties, Weddings. Children's Play Areas. Festival KidZones Organised. Masses of Creative Ideas and In-House Resources.
Simple Shows to Complete Magnificent Packages!

we need this for a marketing event mid october.( 22-23) 2014
i have attached a flyer that is being used at same event to market our tents.
( we may have to make do with images as we have thousands of snap shots but not so many top quality photos! )
we will also be looking for a a3 size poster or two..trying to veer more to contemprorary rather than traditional circus style.
look fwrd to designs!

you are welcome to call / email to discuss.
Updates

sorry. its supposed to be a double sided design. i cant find how to change that!

Thank you for designs so far. I have just added a few more images . if using images of acts/artists i would like to have included an image of our team of African acrobats who are normally in the show. i have put a couple of images that may be useful on the site here. thank you...

Target Market(s)

festival and event bookers.

Industry/Entity Type

Entertainment

Requirements
Must have
• face book , website, twitter links. mobile phone.
Should not have
• too much clip art.

```html
<!DOCTYPE html>
<html lang="en">
<head>
<meta charset="utf-8">
<title>Ringfolly – Circus &amp; Entertainment Flyer</title>
<link href="https://fonts.googleapis.com/css2?family=Roboto+Condensed:wght@300;400;700&display=swap" rel="stylesheet">
<style>
  :root {
    --page: #ffffff;
    --night: #05080a;
    --teal: #1f4a4e;
    --moss: #3d5a2c;
    --silver: #dcdcdc;
    --ink-light: #ffffff;
    --ink-soft: #d4d8d8;
    --strip: rgba(0, 0, 0, 0.45);
  }
  html, body {
    margin: 0;
    padding: 0;
    width: 1200px;
    height: 1000px;
    overflow: hidden;
    background: var(--page);
    font-family: "Roboto Condensed", "Arial Narrow", sans-serif;
  }
  .flyer {
    position: relative;
    width: 1200px;
    height: 1000px;
    background: var(--page);
  }
  .flyer__panel {
    position: absolute;
    left: 0;
    top: 68px;
    width: 1200px;
    height: 854px;
    overflow: hidden;
    background:
      radial-gradient(ellipse 380px 200px at 420px 220px, rgba(61, 90, 44, 0.55), transparent 70%),
      radial-gradient(ellipse 300px 180px at 860px 230px, rgba(61, 90, 44, 0.5), transparent 70%),
      radial-gradient(ellipse 520px 300px at 600px 330px, rgba(31, 74, 78, 0.75), transparent 75%),
      radial-gradient(ellipse 420px 160px at 300px 620px, rgba(31, 74, 78, 0.35), transparent 75%),
      radial-gradient(ellipse 900px 600px at 600px 340px, #12262a, var(--night) 80%);
  }
  .brand {
    position: absolute;
    left: 0;
    top: 250px;
    width: 1200px;
    margin: 0;
    text-align: center;
    font-weight: 700;
    font-size: 168px;
    line-height: 1;
    letter-spacing: 2px;
    color: var(--silver);
  }
  .tagline {
    position: absolute;
    left: 500px;
    top: 508px;
    margin: 0;
    font-weight: 300;
    font-size: 30px;
    color: var(--ink-light);
    white-space: nowrap;
  }
  .tagline strong { font-weight: 700; }
  .headline {
    position: absolute;
    left: 0;
    top: 582px;
    width: 1200px;
    margin: 0;
    text-align: center;
    font-weight: 700;
    font-size: 30px;
    color: var(--ink-light);
    white-space: nowrap;
  }
  .services {
    position: absolute;
    left: 0;
    top: 627px;
    width: 1200px;
    height: 78px;
    background: var(--strip);
    margin: 0;
    padding: 0;
    list-style: none;
  }
  .services__row {
    text-align: center;
    font-weight: 300;
    font-size: 22px;
    line-height: 30px;
    color: var(--ink-soft);
    white-space: nowrap;
  }
  .services__row:first-child { padding-top: 8px; }
  .services__sep { margin: 0 10px; font-size: 16px; vertical-align: 2px; }
  .contacts {
    position: absolute;
    left: 0;
    top: 810px;
    width: 1200px;
    text-align: center;
    font-weight: 300;
    font-size: 22px;
    color: var(--ink-soft);
    white-space: nowrap;
  }
  .contacts__sep { margin: 0 20px; }
</style>
</head>
<body>
<main class="flyer">
  <section class="flyer__panel" role="img" aria-label="Dark night-sky texture in teal and moss green clouds"></section>

  <h1 class="brand">Ringfolly</h1>
  <p class="tagline"><strong>wild</strong> wonders grow under striped roofs!</p>

  <h2 class="headline">Creative Ideas and In-House Resources. Simple Shows to Complete Magnificent Packages!</h2>

  <ul class="services">
    <li class="services__row">Circus Skills Workshops<span class="services__sep">*</span>Acts<span class="services__sep">*</span>Artists &amp; Attractions<span class="services__sep">*</span>Arena Shows<span class="services__sep">*</span>Festivals<span class="services__sep">*</span>Indoor &amp; Outdoor Events</li>
    <li class="services__row">Schools<span class="services__sep">*</span>Parties<span class="services__sep">*</span>Weddings<span class="services__sep">*</span>Children's Play Areas<span class="services__sep">*</span>Festival KidZones Organised</li>
  </ul>

  <p class="contacts">facebook.com/Ringfolly<span class="contacts__sep">|</span>@Ringfolly<span class="contacts__sep">|</span>ringfolly-example.co.uk<span class="contacts__sep">|</span>+44 (0) 1632 960418</p>
</main>
</body>
</html>
```